NEW YORK Plumbing/utility company 10 year anniversary business card

Looking For simple back and front business card would like to include a few things in description
We offer 24/7 emergency service
residential
commercial
industrial
municipal
services offered
Plumbing
hydro excavation
hydro jetting
Well pumps
Sewer pumps
water mains
sewer mains

```html
<!DOCTYPE html>
<html lang="en">
<head>
<meta charset="utf-8">
<title>Riverbend Water &amp; Sewer — Business Card</title>
<link href="https://fonts.googleapis.com/css2?family=Poppins:wght@400;500;600;700&display=swap" rel="stylesheet">
<style>
  :root {
    --stage: #e9e9e9;
    --card-grey: #8e8e8e;
    --ink-grey: #7a7a7a;
    --brand-red: #e41e26;
    --brand-blue: #00aeef;
    --white: #ffffff;
    --text-dark: #2b2b2b;
  }
  * { box-sizing: border-box; margin: 0; padding: 0; }
  html, body {
    width: 1200px; height: 900px; overflow: hidden;
    background: var(--stage);
    font-family: "Poppins", sans-serif;
  }
  .stage {
    width: 1200px; height: 900px;
    display: flex; flex-direction: column; align-items: center; justify-content: center;
    gap: 36px;
  }
  .card {
    position: relative;
    width: 700px; height: 400px;
    box-shadow: 0 6px 18px rgba(0,0,0,.25);
    overflow: hidden;
  }

  /* Back side */
  .card-back {
    background: var(--card-grey);
    color: var(--white);
    display: flex; flex-direction: column; align-items: center;
    padding-top: 62px; text-align: center;
  }
  .brand-mark {
    display: flex; align-items: center; gap: 16px;
    font-weight: 700; letter-spacing: 2px;
  }
  .brand-mark .dot {
    width: 30px; height: 30px; border-radius: 50%;
  }
  .card-back .brand-name { font-size: 54px; color: #d9d9d9; line-height: 1; }
  .card-back .brand-mark .dot { background: #d9d9d9; }
  .brand-sub {
    display: flex; align-items: center; gap: 14px;
    font-weight: 600; letter-spacing: 6px; font-size: 22px;
    color: #555; margin-top: 14px;
  }
  .brand-sub .rule { width: 46px; height: 2px; background: #555; }
  .service-list {
    margin-top: 34px; font-size: 15px; font-weight: 500; letter-spacing: .5px; line-height: 1.6;
  }
  .service-list .drop {
    display: inline-block; width: 7px; height: 9px; margin: 0 6px 0 8px;
    background: var(--white); border-radius: 50% 50% 50% 50% / 60% 60% 40% 40%;
  }
  .divider { width: 250px; height: 1px; background: var(--white); margin: 14px 0 12px; }
  .emergency-line { font-size: 17px; font-weight: 700; letter-spacing: .5px; }

  /* Front side */
  .card-front { background: var(--white); color: var(--text-dark); }
  .swoosh { position: absolute; inset: 0; width: 100%; height: 100%; }
  .contact {
    position: absolute; left: 46px; top: 56px;
    font-size: 18px; line-height: 1.75; letter-spacing: .5px;
  }
  .contact li { list-style: none; display: flex; align-items: center; gap: 10px; }
  .contact svg { width: 16px; height: 16px; flex: none; }
  .markets {
    position: absolute; left: 60px; top: 200px;
    font-size: 17px; line-height: 1.65; letter-spacing: .5px;
  }
  .markets li { list-style: none; display: flex; align-items: center; gap: 10px; }
  .markets li::before {
    content: ""; width: 12px; height: 12px; border-radius: 50%; background: var(--brand-red);
  }
  .front-logo {
    position: absolute; right: 40px; top: 60px; text-align: center;
  }
  .front-logo .brand-name { font-size: 34px; color: var(--brand-red); line-height: 1; }
  .front-logo .brand-mark .dot { background: var(--brand-blue); width: 22px; height: 22px; }
  .front-logo .brand-sub { color: var(--brand-blue); font-size: 16px; letter-spacing: 4px; justify-content: center; margin-top: 10px; }
  .front-logo .brand-sub .rule { background: var(--brand-blue); width: 30px; }
  .front-emergency {
    position: absolute; right: 40px; bottom: 52px; text-align: center;
    color: var(--white); font-size: 20px; font-weight: 500; line-height: 1.3; letter-spacing: .5px;
  }
</style>
</head>
<body>
<main class="stage">

  <section class="card card-back" aria-label="Card back">
    <div class="brand-mark">
      <span class="dot"></span>
      <span class="brand-name">RIVERBEND</span>
    </div>
    <div class="brand-sub"><span class="rule"></span>WATER &amp; SEWER<span class="rule"></span></div>
    <p class="service-list">
      PLUMBING<span class="drop"></span>HYDRO EXCAVATION<span class="drop"></span>HYDRO JETTING<span class="drop"></span>WELL PUMPS<br>
      SEWER PUMPS<span class="drop"></span>WATER MAINS<span class="drop"></span>SEWER MAINS
    </p>
    <div class="divider"></div>
    <p class="emergency-line">WE OFFER 24/7 EMERGENCY SERVICE</p>
  </section>

  <section class="card card-front" aria-label="Card front">
    <svg class="swoosh" viewBox="0 0 700 400" preserveAspectRatio="none" aria-hidden="true">
      <path d="M0 345 C120 355 260 340 420 270 C520 225 600 185 700 170 L700 400 L0 400 Z" fill="#8e8e8e"/>
      <path d="M0 320 C160 330 280 310 420 240 C380 275 320 305 260 320 C170 342 80 346 0 340 Z" fill="#00aeef"/>
      <path d="M0 340 C80 346 170 342 260 320 C320 305 380 275 420 240 C400 262 300 320 0 346 Z" fill="#ffffff"/>
    </svg>

    <ul class="contact">
      <li>
        <svg viewBox="0 0 24 24"><path fill="#00aeef" d="M6.6 10.8a15.1 15.1 0 0 0 6.6 6.6l2.2-2.2a1 1 0 0 1 1-.25 11.4 11.4 0 0 0 3.6.57 1 1 0 0 1 1 1V20a1 1 0 0 1-1 1A17 17 0 0 1 3 4a1 1 0 0 1 1-1h3.5a1 1 0 0 1 1 1c0 1.25.2 2.45.57 3.57a1 1 0 0 1-.25 1z"/></svg>
        555-014-2286 (Office)
      </li>
      <li>
        <svg viewBox="0 0 24 24"><path fill="#00aeef" d="M2 5h20v14H2z"/><path d="M2 5l10 8 10-8" fill="none" stroke="#fff" stroke-width="2"/></svg>
        INFO@RIVERBENDWS.COM
      </li>
      <li>
        <svg viewBox="0 0 24 24"><circle cx="12" cy="12" r="10" fill="none" stroke="#00aeef" stroke-width="2"/><path d="M2 12h20M12 2c3 3 3 17 0 20M12 2c-3 3-3 17 0 20" fill="none" stroke="#00aeef" stroke-width="1.6"/></svg>
        WWW.RIVERBENDWS.COM
      </li>
    </ul>

    <ul class="markets">
      <li>RESIDENTIAL</li>
      <li>COMMERCIAL</li>
      <li>INDUSTRIAL</li>
      <li>MUNICIPAL</li>
    </ul>

    <div class="front-logo">
      <div class="brand-mark">
        <span class="dot"></span>
        <span class="brand-name">RIVERBEND</span>
      </div>
      <div class="brand-sub"><span class="rule"></span>WATER &amp; SEWER<span class="rule"></span></div>
    </div>

    <p class="front-emergency">WE OFFER 24/7<br>EMERGENCY SERVICE</p>
  </section>

</main>
</body>
</html>
```